Visitenkarten-Design für Autorin
Zielgruppe
Ich bin Autorin und schriebe Romane im Genre Romantic Suspense/ romantische Spannungsromane/ Thriller. ich bezeichne meine Geschichten als Herzschlag.
Aufgabenstellung
Details und Vorgaben sind dem angehängten Briefing zu entnehmen,

```html
<!DOCTYPE html>
<html lang="de">
<head>
<meta charset="utf-8">
<title>Visitenkarte – Mia Rosen, Autorin</title>
<link rel="stylesheet" href="https://fonts.googleapis.com/css2?family=Cormorant+Garamond:wght@400;500&display=swap">
<style>
  :root {
    --backdrop: #774c2b;
    --card: #8b6342;
    --card-shadow: rgba(40, 20, 5, 0.45);
    --ink-light: #f4ebe0;
    --ink-soft: #e6d6c4;
    --motif: #a07a57;
    --motif-deep: #96704d;
  }
  * { box-sizing: border-box; margin: 0; padding: 0; }
  html, body {
    width: 1154px;
    height: 1200px;
    overflow: hidden;
    background: var(--backdrop);
  }
  .card-set {
    position: absolute;
    inset: 0;
    display: flex;
    justify-content: center;
    align-items: center;
    gap: 64px;
  }
  .card {
    position: relative;
    width: 450px;
    height: 700px;
    background: var(--card);
    box-shadow: 8px 14px 30px var(--card-shadow);
  }
  /* Front: brand name set in the card's text face */
  .card-front .brand-name {
    position: absolute;
    left: 50%;
    top: 50%;
    transform: translate(-50%, -50%) rotate(90deg);
    font-family: "Cormorant Garamond", serif;
    font-weight: 400;
    font-size: 44px;
    letter-spacing: 12px;
    color: var(--ink-light);
    white-space: nowrap;
  }
  /* Back */
  .card-back .motif {
    position: absolute;
    left: 75px;
    top: 70px;
    width: 300px;
    height: 300px;
    border-radius: 50%;
    background: radial-gradient(circle, var(--motif) 0%, var(--motif-deep) 45%, var(--card) 72%);
  }
  .card-back .identity {
    position: absolute;
    left: 48px;
    bottom: 178px;
    font-family: "Cormorant Garamond", serif;
    color: var(--ink-light);
  }
  .identity .name {
    font-size: 30px;
    font-weight: 500;
    letter-spacing: 1.5px;
    line-height: 1.1;
  }
  .identity .role {
    font-size: 17px;
    letter-spacing: 1px;
    color: var(--ink-soft);
    margin-top: 4px;
  }
  .card-back .contacts {
    position: absolute;
    left: 48px;
    bottom: 60px;
    list-style: none;
    font-family: "Cormorant Garamond", serif;
    font-size: 15px;
    letter-spacing: 1.2px;
    color: var(--ink-soft);
  }
  .contacts li {
    display: flex;
    align-items: center;
    gap: 12px;
    height: 21px;
  }
  .contacts .group-gap { margin-top: 14px; }
  .contacts svg { width: 11px; height: 11px; flex: none; }
</style>
</head>
<body>
  <main class="card-set">
    <section class="card card-front" aria-label="Vorderseite">
      <p class="brand-name">Herzschlag</p>
    </section>

    <section class="card card-back" aria-label="Rückseite">
      <div class="motif" role="img" aria-label="Linienillustration zweier sich haltender Hände mit Strahlenkranz"></div>

      <div class="identity">
        <h1 class="name">Mia Rosen</h1>
        <p class="role">Autorin</p>
      </div>

      <ul class="contacts">
        <li>
          <svg viewBox="0 0 12 12" aria-hidden="true"><rect x="1" y="2.5" width="10" height="7" fill="var(--ink-soft)"/><path d="M1 2.5 6 6.5 11 2.5" fill="none" stroke="var(--card)" stroke-width="1"/></svg>
          mia@mia-rosen.de
        </li>
        <li>
          <svg viewBox="0 0 12 12" aria-hidden="true"><circle cx="6" cy="6" r="5" fill="var(--ink-soft)"/></svg>
          www.mia-rosen.de
        </li>
        <li class="group-gap">
          <svg viewBox="0 0 12 12" aria-hidden="true"><circle cx="6" cy="6" r="4.5" fill="none" stroke="var(--ink-soft)" stroke-width="1.2"/></svg>
          Buchseite: @schreiberinmia
        </li>
        <li>
          <svg viewBox="0 0 12 12" aria-hidden="true"><rect x="1.5" y="1.5" width="9" height="9" fill="none" stroke="var(--ink-soft)" stroke-width="1.2"/></svg>
          Bildkanal: schreiberin_mia
        </li>
      </ul>
    </section>
  </main>
</body>
</html>
```